Business Card Design Project

Hi
I'm currently getting a logo designed which will go on the front. It is designed for s
Fitness instructor/ personal training business.
On the back I would like written:
Boxing for Fitness
Aqua Fitness Professional
PersonalisedTraining 1/1 or Small Group outdoor training
Fun and unique workouts
Weight loss/ Strength training

Also I need on there my details
minaharper27@quillbox.net
0427 395 108
FB Mina Motion

Reason: I would like to extend the deadline to give extra days after I have confirmed the logo in two days

Target Market(s)

Mostly women aged between 20-50

Industry/Entity Type

Training

Font styles to use
Sans Serif

Requirements
Must have
• My logo ( I have attached my favourite logo options )
My details

```html
<!DOCTYPE html>
<html lang="en">
<head>
<meta charset="utf-8">
<title>Mina Motion – Business Card</title>
<link rel="stylesheet" href="https://fonts.googleapis.com/css2?family=Open+Sans:wght@400;600;700&display=swap">
<style>
  :root {
    --blue: #4472bb;
    --orange: #f7a024;
    --white: #ffffff;
    --paper: #efefee;
    --stage: #e4e4e4;
    --text-light: #ffffff;
  }
  * { margin: 0; padding: 0; box-sizing: border-box; }
  html, body {
    width: 1200px; height: 800px; overflow: hidden;
    background: var(--stage);
    font-family: "Open Sans", Arial, sans-serif;
  }
  .sheet {
    position: relative; width: 1200px; height: 800px;
    display: flex; align-items: center; justify-content: center; gap: 60px;
  }
  .card {
    position: relative; width: 520px; height: 300px; overflow: hidden;
    box-shadow: 0 6px 18px rgba(0,0,0,.18);
  }
  /* Logo side */
  .card--logo { background: var(--paper); }
  .card--logo .brand {
    position: absolute; left: 0; right: 0; top: 70px;
    display: flex; align-items: center; justify-content: center; gap: 14px;
  }
  .brand__dot { width: 34px; height: 34px; border-radius: 50%; background: var(--blue); }
  .brand__name { color: var(--blue); font-weight: 600; font-size: 54px; letter-spacing: .5px; }
  .card--logo .fb-line {
    position: absolute; left: 0; right: 0; top: 170px; text-align: center;
    font-size: 50px; font-weight: 400;
  }
  .fb-line .o { color: var(--orange); }
  .fb-line .b { color: var(--blue); }

  /* Details side */
  .card--details { background: var(--blue); }
  .card__bg { position: absolute; inset: 0; }
  .person { position: absolute; left: 188px; top: 32px; color: var(--text-light); }
  .person__name { font-weight: 700; font-size: 15px; line-height: 1.1; }
  .person__role { font-size: 10px; font-weight: 400; }
  .logo-panel {
    position: absolute; left: 170px; top: 72px; width: 250px; height: 128px;
    background: var(--white); text-align: center; padding-top: 20px;
  }
  .logo-panel .brand { display: flex; align-items: center; justify-content: center; gap: 8px; }
  .logo-panel .brand__dot { width: 18px; height: 18px; }
  .logo-panel .brand__name { font-size: 30px; }
  .logo-panel .fb-line { font-size: 26px; margin-top: 14px; white-space: nowrap; }
  .contact {
    position: absolute; left: 112px; top: 222px; list-style: none;
    color: var(--text-light); font-size: 13px;
  }
  .contact li { display: flex; align-items: center; gap: 12px; height: 26px; }
  .contact svg { width: 14px; height: 14px; flex: none; }
</style>
</head>
<body>
<main class="sheet">

  <section class="card card--logo">
    <div class="brand">
      <span class="brand__dot"></span>
      <span class="brand__name">Mina Motion</span>
    </div>
    <p class="fb-line"><span class="o">FB</span> <span class="b">Mina</span> <span class="o">Motion</span></p>
  </section>

  <section class="card card--details">
    <svg class="card__bg" viewBox="0 0 520 300" preserveAspectRatio="none" aria-hidden="true">
      <polygon points="230,0 520,0 520,300 360,300" fill="var(--orange)"/>
      <path d="M0,0 L70,0 Q12,120 0,255 Z" fill="var(--orange)"/>
      <path d="M70,0 Q12,120 0,255" fill="none" stroke="var(--white)" stroke-width="5"/>
      <path d="M520,20 Q430,150 520,290 Z" fill="var(--blue)"/>
      <path d="M520,20 Q430,150 520,290" fill="none" stroke="var(--white)" stroke-width="5"/>
    </svg>

    <div class="person">
      <p class="person__name">Mina harper</p>
      <p class="person__role">Manager</p>
    </div>

    <div class="logo-panel">
      <div class="brand">
        <span class="brand__dot"></span>
        <span class="brand__name">Mina Motion</span>
      </div>
      <p class="fb-line"><span class="o">FB</span> <span class="b">Mina</span> <span class="o">Motion</span></p>
    </div>

    <ul class="contact">
      <li>
        <svg viewBox="0 0 14 14"><rect x="3.5" y="0.5" width="7" height="13" rx="1.2" fill="none" stroke="var(--orange)" stroke-width="1.4"/><rect x="5.5" y="10.5" width="3" height="1.2" fill="var(--orange)"/></svg>
        <span>0427 395 108</span>
      </li>
      <li>
        <svg viewBox="0 0 14 14"><rect x="0.5" y="2.5" width="13" height="9" fill="var(--orange)"/><path d="M0.5,2.5 L7,8 L13.5,2.5" fill="none" stroke="var(--blue)" stroke-width="1.2"/></svg>
        <span>minaharper27@quillbox.net</span>
      </li>
    </ul>
  </section>

</main>
</body>
</html>
```